Gift voucher for a photo shoot, folding card DIN long (21 x 9.8 cm)

Hello, I'm a professional photographer and need a new design for my gift voucher card for a photo shoot. The design should be applicable to all types of photo shoots (neutral). I prefer a sophisticated design. The folded card should be printed on both sides.
My data should be included: Logo, Address: Wendtholzer Strße 27, 07549 Gera, Email: fotograf@malteburgardt.eu, Website: www.malteburgardt.eu Tel.: 0173 / 4958302
Updates

Please design the folding card in DIN long format (105 x 210 mm, landscape format). The card should open horizontally. Please design the front with the words "Gift voucher for you" and my logo. Please make the logo small – the words "Gift voucher" should be in the foreground.
The colors - use elegant gray with gold or white font color.
The inside should contain the words: Photo shoot for ........ worth .....€, as well as my logo.
My contact details should be on the back.

Target Market(s)

Private customer

Colors

Designer to choose only greyscale colors for use in the design.

Requirements
Must have
• Noble appearance, a gift voucher that one likes to give away, words: Gift voucher for you, photo shoot for ..., worth .......€
Nice to have
• Noble appearance of the gift voucher, a gift voucher that you like to give away
Should not have
• no pictures

```html
<!DOCTYPE html>
<html lang="de">
<head>
<meta charset="utf-8">
<title>Gift Voucher – Malte Burgardt Fotograf</title>
<link rel="stylesheet" href="https://fonts.googleapis.com/css2?family=Montserrat:wght@400;600&family=Pinyon+Script&display=swap">
<style>
  :root {
    --backdrop: #c8c9c9;
    --slate: #6c7378;
    --paper: #f7f7f7;
    --ink: #6c7378;
    --white: #ffffff;
  }
  * { box-sizing: border-box; margin: 0; padding: 0; }
  html, body {
    width: 879px;
    height: 1200px;
    overflow: hidden;
  }
  body {
    background: var(--backdrop);
    font-family: "Montserrat", Arial, sans-serif;
    position: relative;
  }
  .card {
    position: absolute;
    left: 209px;
    width: 460px;
    height: 430px;
    box-shadow: 0 6px 18px rgba(0,0,0,0.18);
    display: flex;
    flex-direction: column;
  }
  .card--inside { top: 150px; }
  .card--outside { top: 630px; }

  .panel {
    flex: 0 0 215px;
    height: 215px;
    display: flex;
    flex-direction: column;
    align-items: center;
    justify-content: center;
  }
  .panel--slate { background: var(--slate); color: var(--white); }
  .panel--paper { background: var(--paper); color: var(--ink); }

  .voucher-title { text-align: center; font-weight: 400; }
  .voucher-title__script {
    display: block;
    font-family: "Pinyon Script", cursive;
    font-size: 62px;
    line-height: 62px;
    margin-bottom: 6px;
  }
  .voucher-title__caps {
    display: block;
    font-size: 17px;
    line-height: 20px;
    letter-spacing: 5px;
  }
  .voucher-title__for {
    display: block;
    margin-top: 8px;
    font-size: 11px;
    line-height: 14px;
    letter-spacing: 4px;
    text-transform: uppercase;
  }

  .contact {
    list-style: none;
    text-align: center;
    font-size: 15px;
    letter-spacing: 1.4px;
    line-height: 31px;
  }
  .contact__phone { font-weight: 600; }

  .brand {
    display: flex;
    align-items: center;
    gap: 14px;
  }
  .brand__circle {
    border-radius: 50%;
    border: 2px solid currentColor;
    flex: none;
  }
  .brand__name {
    font-size: 20px;
    letter-spacing: 4px;
    text-transform: uppercase;
    line-height: 1.3;
  }
  .brand--large .brand__circle { width: 46px; height: 46px; }
  .brand--small .brand__circle { width: 24px; height: 24px; }
  .brand--small .brand__name { font-size: 11px; letter-spacing: 3px; }
  .brand__role {
    display: block;
    font-size: 11px;
    letter-spacing: 5px;
  }

  .offer {
    list-style: none;
    text-align: center;
    font-size: 15px;
    letter-spacing: 1.4px;
    line-height: 31px;
    margin-bottom: 22px;
  }
</style>
</head>
<body>

  <section class="card card--inside" aria-label="Gutschein Innenseite">
    <div class="panel panel--slate">
      <h1 class="voucher-title">
        <span class="voucher-title__script">gift</span>
        <span class="voucher-title__caps">VOUCHER</span>
        <span class="voucher-title__for">for you</span>
      </h1>
    </div>
    <div class="panel panel--paper">
      <ul class="contact">
        <li>Wendtholzer Strße 27, 07549 Gera,</li>
        <li>fotograf@malteburgardt.eu</li>
        <li>www.malteburgardt.eu</li>
        <li class="contact__phone">0173 / 4958302</li>
      </ul>
    </div>
  </section>

  <section class="card card--outside" aria-label="Gutschein Außenseite">
    <div class="panel panel--slate">
      <div class="brand brand--large">
        <span class="brand__circle" aria-hidden="true"></span>
        <p class="brand__name">Malte Burgardt<span class="brand__role">Fotograf</span></p>
      </div>
    </div>
    <div class="panel panel--paper">
      <ul class="offer">
        <li>Photo shoot for ................</li>
        <li>worth ........ €</li>
      </ul>
      <div class="brand brand--small">
        <span class="brand__circle" aria-hidden="true"></span>
        <p class="brand__name">Malte Burgardt</p>
      </div>
    </div>
  </section>

</body>
</html>
```